UK landscaping company needs website

We, Brindle Landscapes need a website design for a company based in Surrey, UK. The design should be bold and playful. We have three main areas of work driveways, paving and fencing. It shouldn't be too heavy in text and concentrate on the pictures from previous jobs we've completed. You may use stock images for the design, these can be changed if you are successful. Please don’t just copy the flyer it is just there to provide content.
We have a logo design which we would also like editing slightly.
Here are some of my local competitors
https://www.vexmoorlandscapes.co.uk/

https://www.twinreedgardendesign.com/

https://quarnelllandscapes.co.uk/

Industry/Entity Type

Landscaping

Coding

Coded - Design and coding required

Number of Pages Required

3 page

Font styles to use
Sans Serif

Requirements
Must have
• Pictures of my previous jobs.
Must be mobile friendly
Easy to navigate
Nice to have
• Try to use different colours. It would be good to have some designs that aren’t just black and green.
I’d like some curves in the design.
Should not have
• We install hard landscaping. Think more building/construction and less plants and cutting grass.

```html
<!DOCTYPE html>
<html lang="en">
<head>
<meta charset="utf-8">
<title>Brindle Landscapes</title>
<link href="https://fonts.googleapis.com/css2?family=Poppins:wght@500;700;800&family=Nunito+Sans:wght@400;700&display=swap" rel="stylesheet">
<style>
:root{
  --brick:#c4572e;
  --brick-dark:#a2431f;
  --amber:#f2a33a;
  --slate:#2f3e4e;
  --slate-deep:#1f2a36;
  --sand:#f5ecdc;
  --stone:#d9d3c7;
  --ink:#1f2a36;
  --text:#5f6b76;
  --white:#fff;
}
*{box-sizing:border-box;margin:0;padding:0}
html,body{width:1200px;height:4371px;overflow:hidden}
body{font-family:"Nunito Sans",sans-serif;color:var(--text);background:var(--white)}
h1,h2,h3,h4{font-family:"Poppins",sans-serif;font-weight:700;color:var(--ink)}
.wrap{width:976px;margin:0 auto;position:relative}
.btn{display:inline-block;background:var(--brick);color:#fff;font-family:"Poppins",sans-serif;font-weight:700;font-size:13px;text-transform:uppercase;text-align:center;letter-spacing:.5px;border-radius:30px}
.btn.alt{background:var(--amber);color:var(--slate-deep)}
.photo{display:block}
.wave{position:absolute;left:0;width:1200px;display:block}

/* top bar */
.topbar{height:35px;background:var(--slate-deep);color:var(--stone);font-size:12px;display:flex;align-items:center}
.topbar .wrap{width:1090px;display:flex;align-items:center;gap:30px}
.topbar span{display:flex;align-items:center;gap:8px}
.topbar .social{margin-left:auto;display:flex;gap:14px}
.topbar .social i{width:12px;height:12px;background:var(--amber);border-radius:50%;display:block}

/* nav */
.nav{height:70px;display:flex;align-items:center;background:var(--white)}
.nav .wrap{display:flex;align-items:center}
.logo{display:flex;align-items:center;gap:10px;font-family:"Poppins",sans-serif;font-weight:800;font-size:22px;color:var(--slate)}
.logo i{width:30px;height:30px;border-radius:50%;background:var(--brick);display:block}
.menu{display:flex;gap:30px;margin-left:96px;font-family:"Poppins",sans-serif;font-weight:500;font-size:13px;color:var(--ink)}
.menu span:first-child{color:var(--brick)}
.nav .btn{margin-left:auto;width:178px;height:42px;line-height:42px}

/* hero */
.hero{height:533px;position:relative;background:linear-gradient(100deg,#2b2f36 0%,#5b5550 40%,#9a8a78 68%,#3d3b3a 100%);overflow:hidden}
.hero-copy{position:absolute;left:105px;top:150px}
.hero h1{color:#fff;font-size:54px;line-height:64px;font-weight:800}
.hero h1 em{font-style:normal;color:var(--amber)}
.hero p{color:#f0e8dc;font-size:22px;margin-top:16px}
.hero .btn{width:170px;height:46px;line-height:46px;margin-top:26px}
.hero .arrow{position:absolute;top:250px;width:40px;height:40px;border-radius:50%;background:rgba(255,255,255,.18);color:#fff;font-size:22px;line-height:38px;text-align:center}
.dots{position:absolute;left:580px;top:440px;display:flex;gap:6px}
.dots i{width:8px;height:8px;border-radius:4px;background:rgba(255,255,255,.6)}
.dots i:first-child{width:22px;background:var(--amber)}
.hero .wave{bottom:-1px}

/* who we are */
.about{height:500px;padding-top:52px;position:relative}
.about .wrap{display:flex;align-items:flex-start}
.about .photo{width:475px;height:340px;border-radius:120px 24px 120px 24px;background:linear-gradient(180deg,#a9b7c4 0%,#8a8f93 35%,#b5a48e 65%,#8c7a66 100%);box-shadow:0 16px 30px rgba(31,42,54,.2)}
.about-copy{margin-left:40px;width:460px;padding-top:6px}
.eyebrow{font-family:"Poppins",sans-serif;font-weight:700;font-size:12px;letter-spacing:2px;color:var(--brick);text-transform:uppercase}
.about h2{font-size:34px;margin-top:6px}
.about p{font-size:14px;line-height:23px;margin-top:16px}
.about blockquote{color:var(--brick);font-weight:700;font-size:15px;line-height:23px;margin-top:18px;padding-left:16px;border-left:4px solid var(--amber);border-radius:2px}
.about cite{display:block;margin-top:14px;font-family:"Poppins",sans-serif;font-style:normal;font-weight:500;font-size:15px;color:var(--ink)}
.about .btn{width:170px;height:44px;line-height:44px;margin-top:22px}

/* stats */
.stats{height:294px;background:var(--slate);position:relative;display:flex;align-items:center}
.stats .wrap{display:flex;justify-content:space-between}
.stat{width:210px;height:170px;border-radius:28px;background:rgba(255,255,255,.07);text-align:center;padding-top:26px}
.stat .ico{width:48px;height:48px;background:var(--amber);border-radius:50%;margin:0 auto;display:flex;align-items:center;justify-content:center}
.stat b{display:block;font-family:"Poppins",sans-serif;color:#fff;font-size:36px;line-height:1;margin-top:16px}
.stat span{display:block;color:var(--stone);font-size:13px;margin-top:10px;text-transform:uppercase;letter-spacing:1px;font-weight:700}

/* why choose */
.why{height:606px;padding-top:60px;background:var(--sand)}
.why-head{margin-left:334px}
.why h2{color:var(--slate);font-size:32px}
.why-head p{font-size:14px;line-height:22px;margin-top:10px;width:640px}
.why-body{display:flex;margin-top:30px}
.why-photos .photo{width:308px;height:200px;border-radius:24px;margin-bottom:10px}
.wp1{background:linear-gradient(180deg,#b4c0ca 0%,#8e8b86 45%,#a79a88 100%)}
.wp2{background:linear-gradient(180deg,#9aa9b6 0%,#9c6c52 45%,#b9a78f 100%)}
.features{display:grid;grid-template-columns:1fr 1fr;column-gap:22px;row-gap:22px;margin-left:26px;width:642px;align-content:start}
.feature{background:var(--white);border-radius:24px;padding:22px 22px 20px;height:180px}
.feature .top{display:flex;align-items:center;gap:16px}
.feature .circle{width:52px;height:52px;border-radius:50%;background:var(--brick);display:flex;align-items:center;justify-content:center;flex:none}
.feature:nth-child(even) .circle{background:var(--amber)}
.feature h4{font-size:17px}
.feature p{font-size:13.5px;line-height:21px;margin-top:14px}

/* cta */
.cta{height:346px;background:linear-gradient(120deg,var(--brick) 0%,var(--brick-dark) 100%);position:relative}
.cta-copy{position:absolute;left:112px;top:86px}
.cta h2{color:#fff;font-size:30px}
.cta p{color:#fbe9dd;font-size:14px;line-height:22px;margin-top:16px;width:540px}
.cta .btn{width:170px;height:46px;line-height:46px;margin-top:26px}
.cta .photo{position:absolute;left:697px;top:-40px;width:391px;height:386px;border-radius:160px 24px 24px 24px;background:linear-gradient(180deg,#d3d8dc 0%,#7c6a58 35%,#a9a196 65%,#cfc8bc 100%);box-shadow:0 16px 30px rgba(0,0,0,.25)}

/* services */
.services{height:736px;padding-top:70px;text-align:center}
.sec-title{font-size:34px}
.rule{display:block;margin:14px auto 0}
.sec-sub{font-size:14px;margin-top:14px}
.cards{display:flex;justify-content:space-between;margin-top:40px}
.card{width:308px;border-radius:28px;background:var(--sand);overflow:hidden;height:430px;text-align:center}
.card .photo{height:210px;border-radius:0 0 60px 60px}
.card h4{font-size:19px;margin-top:22px}
.card p{font-size:13.5px;line-height:21px;margin-top:12px;padding:0 22px}
.ph-a{background:linear-gradient(180deg,#a7b6c3 0%,#8b8782 40%,#6d6762 100%)}
.ph-b{background:linear-gradient(180deg,#c7ccd0 0%,#b6ab9a 45%,#938471 100%)}
.ph-c{background:linear-gradient(180deg,#a5c0d8 0%,#7a6046 40%,#5e4a36 100%)}

/* recent */
.recent{height:520px;background:var(--slate-deep);padding-top:70px;text-align:center;position:relative}
.recent .sec-title{color:#fff}
.recent .sec-sub{color:var(--stone)}
.gallery{display:flex;justify-content:center;gap:24px;margin-top:40px}
.gallery .photo{width:220px;height:150px;border-radius:24px}
.g1{background:linear-gradient(180deg,#9aa4ad 0%,#cfcac2 60%,#a8a29a 100%)}
.g2{background:linear-gradient(180deg,#8a6a50 0%,#b3a38c 60%,#9a8d7a 100%)}
.g3{background:linear-gradient(180deg,#c08a78 0%,#d4cfc6 50%,#a6a09a 100%)}
.g4{background:linear-gradient(180deg,#dfe5ea 0%,#8a6a4d 45%,#6e5842 100%)}
.recent .btn{width:160px;height:46px;line-height:46px;margin-top:48px}

/* partners */
.partners{height:187px;background:var(--sand);display:flex;align-items:center}
.partners .wrap{display:flex;justify-content:space-between;padding:0 30px}
.badge{width:110px;height:70px;display:flex;align-items:center;justify-content:center}
.badge i{display:block;width:62px;height:62px;border-radius:50%;background:var(--stone)}
.badge:nth-child(even) i{border-radius:18px;width:96px;height:44px}

/* footer */
.footer{height:492px;background:var(--slate);padding-top:70px}
.footer .wrap{display:flex}
.f-about{width:334px}
.footer .logo{color:#fff}
.footer .logo i{background:var(--amber)}
.f-about p{color:var(--stone);font-size:14px;line-height:22px;margin-top:32px;width:300px}
.f-social{display:flex;gap:8px;margin-top:26px}
.f-social i{width:34px;height:34px;border-radius:50%;background:var(--brick);display:block}
.f-contact{width:334px}
.f-contact h4{color:#fff;font-size:19px;margin-top:4px}
.f-contact hr{width:52px;border:0;border-top:4px solid var(--amber);border-radius:2px;margin:18px 0 24px}
.f-row{display:flex;font-size:13.5px;color:var(--stone);margin-bottom:18px}
.f-row b{width:76px;color:#fff;font-weight:700}
.f-photos .photo{width:308px;height:170px;margin-bottom:12px;border-radius:24px}
.fp1{background:linear-gradient(180deg,#a5b2bf 0%,#9a948c 45%,#857a6c 100%)}
.fp2{background:linear-gradient(180deg,#c5cbd0 0%,#a68f78 45%,#8a7763 100%)}

.copy{height:52px;background:var(--slate-deep);color:var(--stone);font-size:12px;text-align:center;line-height:52px}
</style>
</head>
<body>

<header>
  <div class="topbar">
    <div class="wrap">
      <span><svg width="11" height="11" viewBox="0 0 24 24"><path fill="#f2a33a" d="M6.6 10.8a15 15 0 006.6 6.6l2.2-2.2c.3-.3.7-.4 1-.2 1.1.4 2.3.6 3.6.6.6 0 1 .4 1 1V20c0 .6-.4 1-1 1C10.6 21 3 13.4 3 4c0-.6.4-1 1-1h3.5c.6 0 1 .4 1 1 0 1.3.2 2.5.6 3.6.1.3 0 .7-.2 1z"/></svg>+44-7700-900418</span>
      <span><svg width="11" height="11" viewBox="0 0 24 24"><circle cx="12" cy="12" r="9" fill="none" stroke="#f2a33a" stroke-width="2.5"/><path d="M12 7v5l3 2" stroke="#f2a33a" stroke-width="2.5" fill="none"/></svg>Mon - Sat : 08:00 - 17:00</span>
      <span><svg width="10" height="12" viewBox="0 0 20 24"><path fill="#f2a33a" d="M10 0a8 8 0 00-8 8c0 6 8 16 8 16s8-10 8-16a8 8 0 00-8-8zm0 11a3 3 0 110-6 3 3 0 010 6z"/></svg>Ashcombe Lane, RH1 4QT, Redhill, UK</span>
      <div class="social"><i></i><i></i><i></i><i></i></div>
    </div>
  </div>
  <nav class="nav">
    <div class="wrap">
      <div class="logo"><i></i>Brindle Landscapes</div>
      <div class="menu"><span>Home</span><span>About Us</span><span>Why Choose Us</span><span>Services</span><span>Projects</span><span>Contact Us</span></div>
      <span class="btn">Get Free Quote</span>
    </div>
  </nav>
</header>

<section class="hero" role="img" aria-label="Newly laid block-paved driveway in front of a house">
  <span class="arrow" style="left:20px">&#8249;</span>
  <span class="arrow" style="right:20px">&#8250;</span>
  <div class="hero-copy">
    <h1>High Quality &amp;<br><em>Guaranted</em> Services</h1>
    <p>Making your surroundings beautiful</p>
    <span class="btn alt">Hire Us Now</span>
  </div>
  <div class="dots"><i></i><i></i><i></i></div>
  <svg class="wave" height="70" viewBox="0 0 1200 70" preserveAspectRatio="none"><path d="M0 40C200 0 400 0 600 30s400 40 600 0V70H0z" fill="#fff"/></svg>
</section>

<section class="about">
  <div class="wrap">
    <div class="photo" role="img" aria-label="Sandstone patio paving with a brick edge"></div>
    <div class="about-copy">
      <div class="eyebrow">About us</div>
      <h2>Who We Are</h2>
      <p>We provide a wide range of services in the field of paving &amp; brickwork, driveways, fencing and landscaping. We build the outdoor spaces that add value and beauty to your home, and we focus on our clients' satisfaction.</p>
      <blockquote>Our aim is to enhance the exterior look of your house, and raise the value of your property.</blockquote>
      <cite>— Brindle Landscapes</cite>
      <span class="btn">Our Projects</span>
    </div>
  </div>
</section>

<section class="stats">
  <div class="wrap">
    <div class="stat"><div class="ico"><svg width="22" height="22" viewBox="0 0 24 24"><path d="M5 12l5 5 9-10" stroke="#1f2a36" stroke-width="3" fill="none"/></svg></div><b>212</b><span>Project Complete</span></div>
    <div class="stat"><div class="ico"><svg width="22" height="22" viewBox="0 0 24 24"><path d="M12 21s-8-5-8-11a4 4 0 018-1 4 4 0 018 1c0 6-8 11-8 11z" fill="#1f2a36"/></svg></div><b>100</b><span>Happy Costumer</span></div>
    <div class="stat"><div class="ico"><svg width="22" height="22" viewBox="0 0 24 24"><path d="M5 8h11v6a5 5 0 01-5 5h-1a5 5 0 01-5-5zM16 10h2a2 2 0 010 4h-2" stroke="#1f2a36" stroke-width="2.4" fill="none"/></svg></div><b>521</b><span>Cup of Coffee</span></div>
    <div class="stat"><div class="ico"><svg width="22" height="22" viewBox="0 0 24 24"><circle cx="12" cy="8" r="4" fill="#1f2a36"/><path d="M4 21a8 8 0 0116 0z" fill="#1f2a36"/></svg></div><b>225</b><span>Employer</span></div>
  </div>
</section>

<section class="why">
  <div class="wrap">
    <div class="why-head">
      <div class="eyebrow">Why us</div>
      <h2>Who Choose Us?</h2>
      <p>We have experienced team, through innovation and technology, we are able to provide a top quality, on-demand response to all your landscaping needs.</p>
    </div>
    <div class="why-body">
      <div class="why-photos">
        <div class="photo wp1" role="img" aria-label="Grey block paving driveway"></div>
        <div class="photo wp2" role="img" aria-label="Brick retaining wall with patio steps"></div>
      </div>
      <div class="features">
        <div class="feature"><div class="top"><div class="circle"><svg width="20" height="24" viewBox="0 0 20 24"><path fill="#fff" d="M10 0a8 8 0 00-8 8c0 6 8 16 8 16s8-10 8-16a8 8 0 00-8-8zm0 11a3 3 0 110-6 3 3 0 010 6z"/></svg></div><h4>The Best in Area</h4></div><p>We provide end to end design services for your landscaping needs.</p></div>
        <div class="feature"><div class="top"><div class="circle"><svg width="22" height="22" viewBox="0 0 24 24"><path d="M5 12l5 5 9-10" stroke="#1f2a36" stroke-width="3" fill="none"/></svg></div><h4>Certified Expert</h4></div><p>We have experienced team, through innovation and technology, we are able to provide a top quality, on-demand response to all your landscaping needs.</p></div>
        <div class="feature"><div class="top"><div class="circle"><svg width="22" height="22" viewBox="0 0 24 24"><path d="M12 3v18M7 8h7a3 3 0 010 6H9a3 3 0 000 6h8" stroke="#fff" stroke-width="2.4" fill="none"/></svg></div><h4>Affordabel Pricing</h4></div><p>A fair and reasonable price for world class landscaping &amp; other services.</p></div>
        <div class="feature"><div class="top"><div class="circle"><svg width="22" height="22" viewBox="0 0 24 24"><path d="M12 2l3 7 7 .6-5.4 4.7 1.7 7.2L12 17.8 5.7 21.5l1.7-7.2L2 9.6 9 9z" fill="#1f2a36"/></svg></div><h4>High Quality Services</h4></div><p>We provide high quality paving, driveways and fencing services.</p></div>
      </div>
    </div>
  </div>
</section>

<section class="cta">
  <div class="cta-copy">
    <h2>Planning a New Driveway?</h2>
    <p>Sed orci dolor, pulvinar nec luctus a, malesuada ac nisl. Aliquam eleifend et dui et suscipit. Nam semper accumsan ante, ac dapibus urna dapibus et.</p>
    <span class="btn alt">Contact Now</span>
  </div>
  <div class="photo" role="img" aria-label="Resin driveway with brick border and timber fence"></div>
</section>

<section class="services">
  <div class="wrap">
    <div class="eyebrow">What we build</div>
    <h2 class="sec-title">Our Services</h2>
    <svg class="rule" width="90" height="14" viewBox="0 0 90 14"><path d="M2 7c14-10 29 10 43 0s29-10 43 0" stroke="#c4572e" stroke-width="4" fill="none" stroke-linecap="round"/></svg>
    <p class="sec-sub">Every case is very important to us and we always take care of them seriously.</p>
    <div class="cards">
      <div class="card"><div class="photo ph-a" role="img" aria-label="Block-paved driveway with parked car space"></div><h4>Driveways</h4><p>Block paving, resin, tarmac and gravel driveways built on a solid sub-base, with neat edging and proper drainage to last for years.</p></div>
      <div class="card"><div class="photo ph-b" role="img" aria-label="Natural stone patio slabs with pointed joints"></div><h4>Paving</h4><p>Patios, paths and steps in natural stone, porcelain and brick. Careful levelling and pointing for a clean, hard-wearing finish.</p></div>
      <div class="card"><div class="photo ph-c" role="img" aria-label="Closeboard timber fence on concrete posts"></div><h4>Fencing</h4><p>Closeboard, overlap, picket and slatted fences on concrete or timber posts, plus matching wooden and metal gates.</p></div>
    </div>
  </div>
</section>

<section class="recent">
  <h2 class="sec-title">Recent Project</h2>
  <svg class="rule" width="90" height="14" viewBox="0 0 90 14"><path d="M2 7c14-10 29 10 43 0s29-10 43 0" stroke="#f2a33a" stroke-width="4" fill="none" stroke-linecap="round"/></svg>
  <p class="sec-sub">Start building with Brindle Landscapes</p>
  <div class="gallery">
    <div class="photo g1" role="img" aria-label="Grey paving slab path"></div>
    <div class="photo g2" role="img" aria-label="Brick-edged patio"></div>
    <div class="photo g3" role="img" aria-label="Gravel driveway with kerb edging"></div>
    <div class="photo g4" role="img" aria-label="New timber fence run"></div>
  </div>
  <span class="btn">View More</span>
</section>

<section class="partners">
  <div class="wrap">
    <div class="badge"><i></i></div><div class="badge"><i></i></div><div class="badge"><i></i></div>
    <div class="badge"><i></i></div><div class="badge"><i></i></div><div class="badge"><i></i></div>
  </div>
</section>

<footer class="footer">
  <div class="wrap">
    <div class="f-about">
      <div class="logo"><i></i>Brindle Landscapes</div>
      <p>We provide a wide range of services in the field of driveways, paving and fencing. Help you to build your dream outdoor space.</p>
      <div class="f-social"><i></i><i></i><i></i><i></i><i></i></div>
    </div>
    <div class="f-contact">
      <h4>Contact Info</h4>
      <hr>
      <div class="f-row"><b>Address</b>Ashcombe Lane, RH1 4QT, Redhill, UK</div>
      <div class="f-row"><b>Office</b>+44 7700 900418</div>
      <div class="f-row"><b>Email</b>hello@brindle-landscapes.co.uk</div>
    </div>
    <div class="f-photos" style="margin-left:auto">
      <div class="photo fp1" role="img" aria-label="Block-paved front driveway"></div>
      <div class="photo fp2" role="img" aria-label="Stone patio with brick steps"></div>
    </div>
  </div>
</footer>
<div class="copy">Copyright 2020-21 © Brindle Landscapes</div>

</body>
</html>
```